P.L.U.S.O.N. Content Framework Infographic

I am looking to take my basic infographic to the next level. I need to to translate the content marketing concept that is outlined in the uploaded file. I have attached the content and the image I would like used. I am not stuck on the colors represented in the image but do want to see a variety of options.

Target Market(s)

Companies that are looking for a content marketing strategy, SEO Agencies, marketing agencies

Industry/Entity Type

Digital marketing, SEO

Font styles to use
Other font styles liked:
• arial, calibri are fine

Colors
0054AA
0677BA
7BADD7
CADEEF
E8F1F8
0094D4
00A9DD
6FCCEA
C7EBF8
E9F6FB
00AB8E
00BBA5
67D7C9
C6EFE9
E9F9F6
59FF00
82FF00
B8FF75
E3FFCB
F4FFEA
EE7325
F08F49
F5BC92
FAE3D3
FDF4ED
EB3D1F
EC4F4E
F09395
F8D3D4
FCEDEE

Requirements
Must have
• The image that I provided with the content breakdown with section connectors to the image
Nice to have
• a few different way to present the data

```html
<!DOCTYPE html>
<html lang="en">
<head>
<meta charset="utf-8">
<title>P.L.U.S.O.N. Content Framework</title>
<link href="https://fonts.googleapis.com/css2?family=Outfit:wght@800&family=Montserrat:wght@400;700&family=Roboto:wght@500;700&family=Roboto+Condensed:wght@400;700&display=swap" rel="stylesheet">
<style>
  :root {
    --stage: #f3f3f1;
    --paper: #efefec;
    --panel: #fbfbfa;
    --forest: #1f3b27;
    --lime: #8dc63f;
    --olive: #3d522b;
    --olive-dark: #2b3f2c;
    --leaf: #4b8c36;
    --slate-olive: #4b5142;
    --ink: #2a2a2a;
    --white: #ffffff;
    --stripe: #6fae45;
  }
  * { margin: 0; padding: 0; box-sizing: border-box; }
  html, body { width: 1200px; height: 2978px; overflow: hidden; }
  body { background: var(--stage); position: relative; font-family: "Montserrat", Arial, sans-serif; }

  .poster {
    position: absolute; left: 0; top: 713px;
    width: 996px; height: 1288px;
    transform: scale(1.2048); transform-origin: 0 0;
    background: var(--paper); overflow: hidden;
  }
  .masthead {
    position: absolute; left: 0; top: 0; width: 100%; height: 216px;
    background: var(--forest);
  }
  .headline {
    position: absolute; left: 0; top: 52px; width: 100%;
    text-align: center; color: var(--white);
    font-family: "Outfit", Arial, sans-serif; font-weight: 800;
    font-size: 49px; line-height: 48px; letter-spacing: -0.5px; white-space: nowrap;
  }
  .headline .accent { color: var(--lime); }
  .content-panel {
    position: absolute; left: 66px; top: 207px; width: 864px; height: 1072px;
    background: var(--panel); border-radius: 28px 28px 0 0;
  }
  .tagline {
    position: absolute; left: 289px; top: 178px; width: 386px; height: 44px;
    background: var(--forest); border-radius: 10px;
    color: var(--white); text-align: center;
    font-family: "Roboto", Arial, sans-serif; font-weight: 500; font-size: 30px; line-height: 44px;
  }
  .intro {
    position: absolute; left: 94px; top: 237px; width: 808px;
    text-align: center; color: var(--ink);
    font-size: 11.6px; line-height: 13.8px;
  }
  .intro strong { font-weight: 700; }

  .connectors { position: absolute; left: 0; top: 0; width: 996px; height: 1288px; }

  .pillar { position: absolute; width: 219px; height: 320px; }
  .pillar-icon {
    position: absolute; left: 72px; top: 0; width: 76px; height: 76px;
    border-radius: 50%; background: var(--pillar-color);
    display: flex; align-items: center; justify-content: center;
  }
  .pillar-icon svg { width: 40px; height: 40px; }
  .pillar-title {
    position: absolute; left: 0; top: 61px; width: 219px; height: 49px;
    background: var(--pillar-color); color: var(--white);
    font-family: "Roboto", Arial, sans-serif; font-weight: 700; font-size: 19px;
    line-height: 49px; text-align: center; letter-spacing: 0.2px; white-space: nowrap;
  }
  .pillar-body { position: absolute; left: 17px; top: 110px; width: 185px; height: 200px; }
  .pillar-frame { position: absolute; inset: 0; }
  .pillar-text {
    position: relative; padding: 8px 10px 0;
    font-family: "Roboto Condensed", Arial, sans-serif; font-size: 10px; line-height: 11px;
    color: var(--ink); text-align: center;
  }
  .pillar-text strong { font-weight: 700; display: block; }

  .pillar--expertise { left: 118px; top: 343px; --pillar-color: var(--olive); }
  .pillar--trust { left: 381px; top: 343px; --pillar-color: var(--leaf); }
  .pillar--multimedia { left: 651px; top: 343px; --pillar-color: var(--olive); }
  .pillar--authority { left: 118px; top: 906px; --pillar-color: var(--olive-dark); }
  .pillar--experience { left: 381px; top: 906px; --pillar-color: var(--olive); }
  .pillar--engagement { left: 651px; top: 906px; --pillar-color: var(--slate-olive); }

  .footer-stripe { position: absolute; left: 0; bottom: 0; width: 100%; height: 9px; background: var(--stripe); }
</style>
</head>
<body>
<main class="poster">
  <header class="masthead">
    <h1 class="headline">PUTTING <span class="accent">P.L.U.S.O.N.</span> ON THE BONE<br>FOR THE USER &amp; SEARCHLY TO CHEW ON</h1>
  </header>
  <section class="content-panel"></section>
  <h2 class="tagline">In SEO content is still king</h2>
  <p class="intro">What has changed with content is not the content but the delivery of that content. People these days are consuming content in so many different places &amp; formats that it makes it difficult to create engaging content that ranks and converts. Some people prefer to continue reading webpages to find the information they are looking for. Some prefer to see the pictures because they are more visual than contextual. Others would prefer to just watch video on ClipTube or other online video platforms, and in some cases it is more of an auditory way such as podcast &amp; streaming radio platforms. This infographic will breakdown how all of the pieces fit together to get <strong>“P.L.U.S.O.N”</strong> on the bone of content.</p>

  <svg class="connectors" viewBox="0 0 996 1288">
    <defs>
      <linearGradient id="bodyTone" x1="0" y1="0" x2="1" y2="1">
        <stop offset="0" stop-color="#8aa04f"/>
        <stop offset="0.55" stop-color="#6d8440"/>
        <stop offset="1" stop-color="#4a5a2c"/>
      </linearGradient>
    </defs>
    <rect role="img" aria-label="Illustration of a pig divided into cuts labelled Expertise, Trust, Multimedia, Experience, Authority and Engagement" x="248" y="655" width="528" height="283" rx="120" fill="url(#bodyTone)"/>
    <g fill="none" stroke="#333" stroke-width="1.2" stroke-dasharray="2 2">
      <polyline points="159,626 159,776 294,776"/>
      <polyline points="407,653 407,660"/>
      <polyline points="564,678 844,678 844,644"/>
      <polyline points="408,829 231,829 231,927"/>
      <polyline points="572,800 572,869 496,869 496,927"/>
      <polyline points="681,797 681,863 760,863 760,927"/>
    </g>
    <g fill="#26331f">
      <circle cx="294" cy="776" r="5"/>
      <circle cx="407" cy="660" r="5"/>
      <circle cx="564" cy="678" r="5"/>
      <circle cx="408" cy="829" r="5"/>
      <circle cx="572" cy="800" r="5"/>
      <circle cx="681" cy="797" r="5"/>
    </g>
  </svg>

  <article class="pillar pillar--expertise">
    <div class="pillar-icon"><svg viewBox="0 0 40 40" fill="none" stroke="#fff" stroke-width="2.4" stroke-linecap="round" stroke-linejoin="round"><circle cx="20" cy="11" r="7"/><polyline points="17,11 19.5,13.5 23.5,8.5"/><path d="M4 26l7-5 6 3 6-3 7 2 6 4M11 30l6 5 9-4 4-4"/></svg></div>
    <h3 class="pillar-title">EXPERTISE</h3>
    <div class="pillar-body">
      <svg class="pillar-frame" viewBox="0 0 185 200"><polygon points="2,0 183,0 183,132 92.5,197 2,132" fill="#fff" stroke="#3d522b" stroke-width="3"/></svg>
      <p class="pillar-text"><strong>“Expertise”</strong>refers to the content writer’s level of knowledge or skill in a specific subject area that is relevant to the user’s search query. High-quality content should be created by someone with relevant expertise in the topic being discussed.</p>
    </div>
  </article>

  <article class="pillar pillar--trust">
    <div class="pillar-icon"><svg viewBox="0 0 40 40" fill="none" stroke="#fff" stroke-width="2.4" stroke-linecap="round" stroke-linejoin="round"><path d="M20 3l9 4v7c0 5-4 8-9 10-5-2-9-5-9-10V7z"/><polyline points="16,13 19,16 24,10"/><path d="M4 29l7-4 6 3 6-3 7 2 6 3M11 33l6 4 9-3"/></svg></div>
    <h3 class="pillar-title">TRUSTWORTHINESS</h3>
    <div class="pillar-body">
      <svg class="pillar-frame" viewBox="0 0 185 200"><polygon points="2,0 183,0 183,132 92.5,197 2,132" fill="#fff" stroke="#3d522b" stroke-width="3"/></svg>
      <p class="pillar-text"><strong>“Trustworthiness”</strong>is the final result of doing all of the above. If you can write content that is helpful, knowledge, first hand based on experience from someone who is an expert in their field, you get the trust of users consuming your content. If you can gain the user’s trust about your content. Searchly and other search engines will “Trust” you and will provide you with the organic visibility we all strive for..</p>
    </div>
  </article>

  <article class="pillar pillar--multimedia">
    <div class="pillar-icon"><svg viewBox="0 0 40 40" fill="none" stroke="#fff" stroke-width="2.4" stroke-linecap="round" stroke-linejoin="round"><circle cx="20" cy="24" r="9"/><polyline points="16,24 19,27 24,21"/><path d="M20 3l1.5 3 3 .4-2.2 2 .6 3-2.9-1.5-2.9 1.5.6-3-2.2-2 3-.4zM7 10l1 2 2 .3-1.5 1.4.4 2L7 14.8 5.1 15.7l.4-2L4 12.3l2-.3zM33 10l1 2 2 .3-1.5 1.4.4 2-1.9-.9-1.9.9.4-2-1.5-1.4 2-.3z"/></svg></div>
    <h3 class="pillar-title">MULTIMEDIA</h3>
    <div class="pillar-body">
      <svg class="pillar-frame" viewBox="0 0 185 200"><polygon points="2,0 183,0 183,132 92.5,197 2,132" fill="#fff" stroke="#3d522b" stroke-width="3"/></svg>
      <p class="pillar-text"><strong>“Multimedia”</strong>consists of infographics, specific images, embedded videos, and other types content aside from the written word. By doing this you provide the same content to audiences that differ based on how they choose to consume content. Online content marketing with multimedia is highly engaging as it presents desired information in a multifaceted but direct and timely manner.</p>
    </div>
  </article>

  <article class="pillar pillar--authority">
    <div class="pillar-icon"><svg viewBox="0 0 40 40" fill="none" stroke="#fff" stroke-width="2.4" stroke-linecap="round" stroke-linejoin="round"><rect x="17" y="4" width="16" height="20" rx="1"/><path d="M21 9h8M21 13h8M21 17h5"/><circle cx="12" cy="20" r="4"/><path d="M4 36c0-6 4-9 8-9s7 2 8 5l6-3"/></svg></div>
    <h3 class="pillar-title">AUTHORITATIVENESS</h3>
    <div class="pillar-body">
      <svg class="pillar-frame" viewBox="0 0 185 200"><polygon points="2,0 183,0 183,132 92.5,197 2,132" fill="#fff" stroke="#2b3f2c" stroke-width="3"/></svg>
      <p class="pillar-text"><strong>“Authoritativeness”</strong>refers to the credibility of the content and the website it is hosted on. Authoritativeness can be established through the quality of the content, the site’s reputation, author’s reputation, external links &amp; content citations, and the credentials of the content creator.</p>
    </div>
  </article>

  <article class="pillar pillar--experience">
    <div class="pillar-icon"><svg viewBox="0 0 40 40" fill="#fff"><circle cx="20" cy="17" r="4.5"/><path d="M12 33c0-6 3.5-9 8-9s8 3 8 9z"/><circle cx="9" cy="20" r="3.5"/><path d="M2 33c0-5 3-7 7-7 1.5 0 2.5.3 3.3.8C11 28.5 10.5 31 10.5 33z"/><circle cx="31" cy="20" r="3.5"/><path d="M38 33c0-5-3-7-7-7-1.5 0-2.5.3-3.3.8 1.3 1.7 1.8 4.2 1.8 6.2z"/><path d="M20 3l1.2 2.4 2.6.4-1.9 1.8.5 2.6L20 9l-2.4 1.2.5-2.6-1.9-1.8 2.6-.4zM10 7l1 2 2 .3-1.5 1.4.4 2L10 11.8 8.1 12.7l.4-2L7 9.3l2-.3zM30 7l1 2 2 .3-1.5 1.4.4 2-1.9-.9-1.9.9.4-2L27 9.3l2-.3z"/></svg></div>
    <h3 class="pillar-title">EXPERIENCE</h3>
    <div class="pillar-body">
      <svg class="pillar-frame" viewBox="0 0 185 200"><polygon points="2,0 183,0 183,132 92.5,197 2,132" fill="#fff" stroke="#3d522b" stroke-width="3"/></svg>
      <p class="pillar-text"><strong>“Experience”</strong>In short means that Searchly values firsthand or life experience of the author on the topic a page is about. It is important because often searchers want to know first-hand information before they decide to purchase something or use a certain service.</p>
    </div>
  </article>

  <article class="pillar pillar--engagement">
    <div class="pillar-icon"><svg viewBox="0 0 40 40" fill="none" stroke="#fff" stroke-width="2.4" stroke-linecap="round" stroke-linejoin="round"><circle cx="13" cy="8" r="3.5"/><circle cx="27" cy="8" r="3.5"/><path d="M7 20c0-4 2.5-6 6-6s6 2 6 6M21 20c0-4 2.5-6 6-6s6 2 6 6"/><path d="M4 30l7-5 6 3 6-3 7 2 6 3M11 34l6 4 9-3"/></svg></div>
    <h3 class="pillar-title">ENGAGEMENT</h3>
    <div class="pillar-body">
      <svg class="pillar-frame" viewBox="0 0 185 200"><polygon points="2,0 183,0 183,132 92.5,197 2,132" fill="#fff" stroke="#4b5142" stroke-width="3"/></svg>
      <p class="pillar-text"><strong>“Engagement”</strong>is essential for views and conversion as it keeps readers locked in on content to the point that they are more likely to move through the website experience and at least consider the value offered in the minutes, hours, days, and weeks that follow their website visit.</p>
    </div>
  </article>

  <div class="footer-stripe"></div>
</main>
</body>
</html>
```